Tarek & Lubna's 50th Anniversary Celebration & Reunion

I need a flyer to send out via email and for posting on chatterboard to invite guests to a 50th wedding anniversary / family reunion.

Location is sunny La Jolla CA the Pearl of San Diego's Shore.

Week long daily activities starting Mon July 28-Aug 1st Friday, The event will be on Wednesday.
* Daily Catered Family Breakfast at the Marlow Hall of La Jolla
* Daily group activities including
*Exploring La Jolla Beaches & Ocean Cave Kayaking
*TideRealm Private Behind the Scenes Tour
*World Famous Pellham Wildlife Park
*Sunset Balloon Ride
*Private Yatch on the Bay

Actual Anniversary event will take place Thursday December 28, 2013 at 5pm at the Marlow Hall.

There are many local hotels around the Marlow Hall. 4213 Brindle Ln, La Jolla, CA 92058

Host is Kamil and the entire Haddour Family. For questions, please email Kamil@thelinden-feasts.com

Target Market(s)

all ages from 10 year olds to 70 year olds. Should appeal to all

Industry/Entity Type

Wedding

Font styles to use
Script

Colors

Designer to choose colors to be used in the design.

Requirements
Must have
• Fun graphics, including one with a stretch limo as there will be one available

Photo enclosed
Nice to have
• Logo for TideRealm Inserting a picture of an actual wedding 50 years ago or so of the bride and groom. incorporating the limo cropped out of the picture attached would also be nice

```html
<!DOCTYPE html>
<html lang="en">
<head>
<meta charset="utf-8">
<title>Tarek &amp; Lubna – 50th Anniversary &amp; Family Reunion</title>
<link rel="stylesheet" href="https://fonts.googleapis.com/css2?family=Cinzel+Decorative:wght@900&family=Pinyon+Script&family=Great+Vibes&family=Didact+Gothic&family=Arimo:wght@700&display=swap">
<style>
  :root {
    --coral: #ee4b4b;
    --coral-deep: #e23a3f;
    --lime: #d3de36;
    --ink: #111111;
    --white: #ffffff;
    --frame: #4a4a4a;
    --partner: #0b4d8c;
  }
  html, body { margin: 0; padding: 0; overflow: hidden; }
  body { width: 927px; height: 1200px; background: var(--lime); }
  .flyer {
    position: relative; width: 927px; height: 1200px; overflow: hidden;
    background: var(--lime); color: var(--ink);
    font-family: "Didact Gothic", "Century Gothic", sans-serif;
  }
  .backdrop { position: absolute; inset: 0; }
  .headline {
    position: absolute; left: 40px; top: 4px; margin: 0; white-space: nowrap;
    font-family: "Cinzel Decorative", serif; font-weight: 900;
    font-size: 70px; line-height: 84px; letter-spacing: 1px; color: var(--coral-deep);
    text-shadow: 4px 4px 0 var(--white), 6px 7px 6px rgba(0,0,0,.35);
  }
  .tagline {
    position: absolute; right: 12px; top: 72px; margin: 0; white-space: nowrap;
    font-family: "Great Vibes", cursive; font-size: 48px; line-height: 56px; color: var(--white);
    text-shadow: 2px 2px 3px rgba(0,0,0,.4);
  }
  .section-title {
    font-family: "Pinyon Script", cursive; font-weight: 400; margin: 0; white-space: nowrap;
    color: var(--ink); text-shadow: 1px 0 0 var(--ink), 0 1px 0 var(--ink);
  }
  .activities-title { position: absolute; left: 140px; top: 160px; font-size: 56px; line-height: 64px; }
  .activity-list {
    position: absolute; right: 12px; top: 240px; margin: 0; padding: 0;
    list-style: none; text-align: right; font-size: 27px; line-height: 27px; white-space: nowrap;
  }
  .activity-list li { margin-bottom: 28px; }
  .activity-list li.single { margin-bottom: 27px; }
  .limo { position: absolute; left: 0; top: 462px; width: 386px; height: 92px; }
  .partner {
    position: absolute; right: 15px; top: 640px;
    display: flex; align-items: center; gap: 8px;
    font-family: "Arimo", sans-serif; font-weight: 700; font-size: 24px; color: var(--partner);
  }
  .partner .dot { width: 16px; height: 16px; border-radius: 50%; background: var(--partner); }
  .event-title { position: absolute; left: 12px; top: 590px; font-size: 56px; line-height: 70px; }
  .event-details {
    position: absolute; left: 10px; top: 686px; margin: 0;
    font-size: 27px; line-height: 30px;
  }
  .event-details p { margin: 0 0 31px; }
  .host {
    position: absolute; left: 10px; top: 950px; margin: 0;
    font-family: "Arimo", sans-serif; font-weight: 700; font-size: 19px; line-height: 23px;
  }
  .contact { position: absolute; left: 10px; top: 1010px; margin: 0; font-family: "Arimo", sans-serif; font-weight: 700; }
  .contact .label { display: block; font-size: 22px; line-height: 26px; }
  .contact .email { display: block; font-size: 16px; line-height: 20px; }
  .hotel-note {
    position: absolute; left: 10px; top: 1080px; margin: 0; width: 205px;
    font-family: "Arimo", sans-serif; font-weight: 700; font-size: 12px; line-height: 14px;
  }
  .couple-photo { position: absolute; left: 424px; top: 682px; width: 424px; height: 424px; }
  .couple-names {
    position: absolute; left: 632px; top: 1108px; margin: 0;
    font-family: "Pinyon Script", cursive; font-size: 50px; line-height: 50px; color: var(--ink);
    text-shadow: 1px 0 0 var(--ink);
    transform: rotate(-35deg); transform-origin: left top; white-space: nowrap;
  }
  .dates-note { position: absolute; left: 8px; top: 1166px; margin: 0; font-size: 19px; line-height: 24px; white-space: nowrap; }
  sup { font-size: .55em; line-height: 0; }
</style>
</head>
<body>
<main class="flyer">
  <svg class="backdrop" width="927" height="1200" viewBox="0 0 927 1200" aria-hidden="true">
    <defs>
      <radialGradient id="flare" cx="50%" cy="50%" r="50%">
        <stop offset="0" stop-color="#fff" stop-opacity=".95"/>
        <stop offset=".25" stop-color="#ffd3c8" stop-opacity=".6"/>
        <stop offset="1" stop-color="#ff7a6a" stop-opacity="0"/>
      </radialGradient>
    </defs>
    <path d="M0,144 C303,197 636,424 927,712 V1200 H0 Z" fill="var(--coral)"/>
    <circle cx="667" cy="910" r="280" fill="var(--lime)"/>
    <rect x="0" y="1158" width="927" height="42" fill="var(--lime)"/>
    <circle cx="98" cy="318" r="70" fill="url(#flare)"/>
  </svg>

  <h1 class="headline">Join us in La Jolla!</h1>
  <p class="tagline">the pearl of San Diegos shore</p>

  <h2 class="section-title activities-title">Week Long Family Reunion Activities</h2>
  <ul class="activity-list">
    <li>Daily catered family breakfast at the<br>Marlow Hall of La Jolla</li>
    <li>Exploring La Jolla Beaches and<br>Ocean Cave Kayaking</li>
    <li class="single">TideRealm Private Behind the Scenes Tour</li>
    <li class="single">World Famous Pellham Wildlife Park</li>
    <li class="single">Sunset Balloon Ride</li>
    <li class="single">Private Yacht on the Bay</li>
  </ul>

  <svg class="limo" viewBox="0 0 386 92" role="img" aria-label="Black stretch limousine">
    <rect x="0" y="10" width="386" height="72" rx="20" fill="#1a1a1a"/>
  </svg>

  <div class="partner"><span class="dot"></span>TideRealm</div>

  <h2 class="section-title event-title">50<sup>th</sup> Anniversary Celebration</h2>
  <div class="event-details">
    <p>Wednesday July 30<sup>th</sup>, 2013</p>
    <p>5:00 PM</p>
    <p>Marlow Hall of La Jolla</p>
    <p>4213 Brindle Ln, La Jolla, Ca<br>92058</p>
  </div>

  <p class="host">Hosted by Kamil and<br>the Haddour Family</p>
  <p class="contact">
    <span class="label">For questions please email</span>
    <span class="email">kamil@thelinden-feasts.com</span>
  </p>
  <p class="hotel-note">There are several local hotels located near the Marlow Hall for your convenience.</p>

  <svg class="couple-photo" viewBox="0 0 424 424" role="img" aria-label="Black and white wedding photograph of the bride and groom, fifty years ago">
    <defs>
      <radialGradient id="photoTone" cx="50%" cy="45%" r="60%">
        <stop offset="0" stop-color="#e6e6e6"/>
        <stop offset="1" stop-color="#7d7d7d"/>
      </radialGradient>
    </defs>
    <circle cx="212" cy="212" r="206" fill="url(#photoTone)" stroke="var(--frame)" stroke-width="8"/>
  </svg>
  <p class="couple-names">Tarek &amp; Lubna</p>

  <p class="dates-note">activities will begin on July 28<sup>th</sup> and commence on August 1<sup>st</sup></p>
</main>
</body>
</html>
```